Web Design job - NetQuarry Company including Desktop & Mobile version

Create a Web Design (Uncoded - PSD layout only)

1. About our company

NetQuarry is an Australian-based company which sells used networking devices to coporates and other brokers in USA, Europe and other countries. We are the market leader in this space and currently have warehouses in Sydney and California. Most of our products are from VORTEL.

Our competitive advantages come from lowest price in the market, flexible product configuration for different demands of customers, long time experience in the business and huge stock of inventory.

We are in need of a new website to enhance customer and partner engagement which are measured by sales metrics and website performance metrics such as number of request for a quote, number of new orders, return visits, views, conversion rate, etc.

2. Website structure:

We need different looks for different devices: Desktop, iPad and Mobile with popular screen resolutions for each of following page.

Try to make one as good as possible, then we can move further. Below are the main pages of the web:

+ Home Page: Where customers learn about the company and its business. Should have: Beautiful company profile, highlighted company contact and strengths; A comprehensive overview about selling products.

+ Category Page: Where customers learn about products in a category and do the search action. Should focus on filter and sort functions for easily finding a product.

+ Product Page: Where customers learn about the details of a specific products such as price, image, description, related products.
- Also need features for cross-sell or up-sell.
- An item may have both new and refurbished prices, or either or none of them. Should have options to choose between new or refurbished price to add to cart.

+ Information Page: About the company, Company Announcement.

+ Cart management and Check-out

+ Search results

REFERENCES
Current website: http://netquarry-example.com.au/

Prefered Layout:
- https://www.gearbazaar-example.com/en/vortel-systems/vortel-router-series/vortel-series-1900/vortel-systems-vortel1941-k9
- https://www.wireandcrate-example.com/vortel-2port-rj48-multiflex-t1-trunk-card-vwic2mftt1-p-1374.html
- The attached files play as wireframes, only for the purpose of guiding. You are free to make your choices of colors and layouts.

Target Market(s)

- Corporate clients
- Main market: Australia

Industry/Entity Type

It Company

Number of Pages Required

3 page

Font styles to use
Sans Serif

Requirements
Must have
• - The new design should have a clear look to easily find information while should look professional to aim at corporate clients.
• - Require least time or effort to finish a task
• - Optimize for SEO and loading time
• - Mobile version is optimized for touching, swiping and loading time.
• - Bear in mind that the new website need minimum effort of manual tasks such as updating content. We don’t have human resources for these yet.
Nice to have
• - Should have design for each scenario such as click, popup, dropdown, deactive, have/not have an object

```html
<!DOCTYPE html>
<html lang="en">
<head>
<meta charset="utf-8">
<title>NetQuarry – Networking Equipment</title>
<link href="https://fonts.googleapis.com/css2?family=Montserrat:wght@500;600;700&family=Open+Sans:wght@400;600;700&display=swap" rel="stylesheet">
<style>
:root{
  --orange:#f7892e;
  --orange-dark:#ec7418;
  --orange-soft:#f9c9a0;
  --blue:#0b74c7;
  --blue-dark:#0654a8;
  --blue-deep:#0a3f8c;
  --ink:#222;
  --muted:#555;
  --footer:#0e0e0e;
  --white:#fff;
}
*{box-sizing:border-box;margin:0;padding:0}
html,body{width:1200px;height:3468px;overflow:hidden;background:#fff}
body{position:relative;font-family:'Open Sans',Arial,sans-serif;color:var(--ink)}
.abs{position:absolute}
.heading{font-family:'Montserrat',Arial,sans-serif}

/* top bar */
.topbar{left:0;top:0;width:1200px;height:46px;background:#fff}
.topbar-contact{top:12px;font-size:14px;color:var(--blue-dark);display:flex;align-items:center;gap:7px;white-space:nowrap}
.quote-tab{left:842px;top:0;width:278px;height:50px;background:var(--orange);color:#fff;font-family:'Montserrat',sans-serif;font-weight:600;font-size:22px;display:flex;align-items:center;justify-content:center;gap:14px;border-radius:0 0 10px 10px}

/* nav */
.nav{left:0;top:46px;width:1200px;height:92px;background:#fff;border-bottom:1px solid #eee}
.logo{left:76px;top:16px;display:flex;align-items:center;gap:14px}
.logo .dot{width:62px;height:62px;border-radius:50%;background:var(--orange)}
.logo .name{font-family:'Montserrat',sans-serif;font-weight:700;font-size:36px;color:var(--blue-dark)}
.menu{left:388px;top:42px;display:flex;gap:24px;font-family:'Montserrat',sans-serif;font-size:14px;color:#444;font-weight:500;white-space:nowrap}
.menu .active{color:var(--orange)}
.nav-icon{top:28px;width:52px;height:52px;border-radius:50%;display:flex;align-items:center;justify-content:center}

/* hero */
.hero{left:0;top:138px;width:1200px;height:540px;background:radial-gradient(ellipse at 60% 50%,#1f8ee0 0%,#0b6bc6 45%,#0651a4 100%)}
.hero-product{left:155px;top:58px;width:380px;height:400px;background:linear-gradient(135deg,#5a5f66,#2b2f35 60%,#8c9097);border-radius:4px}
.hero-title{left:580px;top:200px;font-size:52px;font-weight:700;color:#fff;font-family:'Montserrat',sans-serif;white-space:nowrap}
.hero-sub{left:590px;top:276px;font-size:20px;color:#fff}
.btn-orange{background:var(--orange);color:#fff;font-family:'Montserrat',sans-serif;font-weight:600;border-radius:30px;display:flex;align-items:center;justify-content:center;gap:12px}
.btn-orange .mark{width:44px;height:44px;border-radius:50%;background:var(--blue-dark);border:3px solid #fff}
.dots{left:532px;top:502px;display:flex;gap:12px}
.dots span{width:17px;height:17px;border-radius:50%;border:2px solid #fff}
.dots .on{background:var(--orange);border-color:var(--orange)}

/* promo */
.promo{top:724px;width:350px;height:208px;color:#fff;text-align:center}
.promo .thumb{margin:28px auto 0;width:200px;height:80px;border-radius:3px}
.promo .pname{font-family:'Montserrat',sans-serif;font-weight:600;font-size:17px;margin-top:14px}
.promo .save{font-family:'Montserrat',sans-serif;font-weight:700;font-size:30px;margin-top:2px}

.section-title{left:0;width:1200px;text-align:center;font-family:'Montserrat',sans-serif;font-weight:600;font-size:40px;color:var(--blue)}

/* categories */
.cat{top:1077px;width:254px;height:287px;border:1px solid #e5e5e5;background:#fff}
.cat .img{position:absolute;left:14px;top:16px;width:224px;height:196px}
.cat .label{position:absolute;left:0;bottom:0;width:100%;height:56px;color:#fff;font-family:'Montserrat',sans-serif;font-weight:600;font-size:17px;display:flex;align-items:center;justify-content:center;background:linear-gradient(#1180d4,#0652a3)}
.cat .label.warm{background:var(--orange)}

/* quote band */
.quote-band{left:76px;top:1445px;width:1048px;height:363px;background:linear-gradient(100deg,#f7892e,#f59a45)}
.agent{left:670px;top:1398px;width:410px;height:410px}
.quote-title{left:128px;top:1476px;font-family:'Montserrat',sans-serif;font-weight:600;font-size:40px;color:var(--blue-dark)}
.quote-line{display:flex;align-items:center;gap:20px;color:#fff;white-space:nowrap}

/* stats */
.stat{top:1952px;width:220px;text-align:center}
.stat svg{display:block;margin:0 auto}
.stat .label{font-size:18px;color:#222;margin-top:14px;line-height:1.5;font-weight:600;text-transform:uppercase;letter-spacing:.2px}

/* about */
.about{left:76px;top:2217px;width:1048px;height:289px;background:linear-gradient(90deg,#0b74c7,#0b4fa0)}
.about h2{position:absolute;left:32px;top:32px;font-family:'Montserrat',sans-serif;font-weight:600;font-size:40px;color:#fff}
.about p{position:absolute;left:32px;width:760px;font-size:14.5px;line-height:1.75;color:#fff}

/* why */
.why{top:2656px;width:350px;height:210px;color:#fff;text-align:center}
.why .ico{position:absolute;left:125px;top:22px}
.why .label{position:absolute;left:0;width:100%;top:162px;font-family:'Montserrat',sans-serif;font-weight:600;font-size:20px}

/* footer */
.waves{left:0;top:2910px;width:1200px;height:110px}
.footer{left:0;top:3016px;width:1200px;height:388px;background:var(--footer);color:#ddd}
.footer h4{position:absolute;top:26px;font-family:'Montserrat',sans-serif;font-weight:500;font-size:18px;color:var(--orange)}
.footer .txt{position:absolute;font-size:14.5px;line-height:1.8;color:#d6d6d6}
.frow{position:absolute;display:flex;align-items:flex-start;gap:16px;font-size:14.5px;line-height:1.6}
.why-row{position:absolute;left:874px;display:flex;align-items:center;gap:18px;font-size:14px}
.why-row .b{width:44px;height:44px;border-radius:50%;background:var(--blue);display:flex;align-items:center;justify-content:center;color:#fff;font-weight:700;font-size:11px}
.card{width:66px;height:40px;border-radius:4px}
.bottom{left:0;top:3404px;width:1200px;height:64px;background:var(--orange);color:#fff;font-size:15px;display:flex;align-items:center;justify-content:center}
</style>
</head>
<body>

<!-- top bar -->
<div class="abs topbar"></div>
<div class="abs topbar-contact" style="left:408px">
  <svg width="17" height="17" viewBox="0 0 24 24"><circle cx="12" cy="12" r="12" fill="#f7892e"/><path d="M8 6l2 0 1 3-1.5 1a7 7 0 0 0 4 4l1-1.5 3 1v2a2 2 0 0 1-2 1A10 10 0 0 1 7 8a2 2 0 0 1 1-2z" fill="#fff"/></svg>
  <span>(+61) 02 5550 1234</span>
</div>
<div class="abs topbar-contact" style="left:588px">
  <svg width="18" height="14" viewBox="0 0 20 16"><rect x="1" y="1" width="18" height="14" rx="2" fill="none" stroke="#0654a8" stroke-width="1.6"/><path d="M1 2l9 7 9-7" fill="none" stroke="#0654a8" stroke-width="1.6"/></svg>
  <span>hello@netquarry-example.com</span>
</div>
<div class="abs quote-tab">REQUEST A QUOTE <svg width="16" height="10" viewBox="0 0 16 10"><path d="M0 0h16L8 10z" fill="#fff"/></svg></div>

<!-- navigation -->
<header class="abs nav">
  <div class="abs logo"><span class="dot"></span><span class="name">NetQuarry</span></div>
  <nav class="abs menu">
    <span class="active">HOME</span><span>ROUTERS</span><span>SWITCHES</span><span>WIRELESSES</span><span>IP PHONES</span><span>ACCESSORIES</span>
  </nav>
  <div class="abs nav-icon" style="left:1018px;border:2px solid #ddd">
    <svg width="22" height="22" viewBox="0 0 22 22"><circle cx="9" cy="9" r="6.5" fill="none" stroke="#999" stroke-width="2.4"/><path d="M14 14l6 6" stroke="#999" stroke-width="2.6"/></svg>
  </div>
  <div class="abs nav-icon" style="left:1076px;background:var(--orange)">
    <svg width="26" height="24" viewBox="0 0 26 24"><path d="M1 2h4l3 13h13l3-9H7" fill="none" stroke="#fff" stroke-width="2.4"/><circle cx="10" cy="20" r="2" fill="#fff"/><circle cx="19" cy="20" r="2" fill="#fff"/></svg>
  </div>
</header>

<!-- hero -->
<section class="abs hero">
  <div class="abs hero-product" role="img" aria-label="Rack-mounted network chassis with switch modules"></div>
  <div class="abs hero-title">SAVE UP TO 40%</div>
  <div class="abs hero-sub">By doing business with NetQuarry</div>
  <div class="abs btn-orange" style="left:584px;top:326px;width:210px;height:58px;font-size:20px;justify-content:space-between;padding:0 8px 0 30px">STOK LIST <span class="mark"></span></div>
  <div class="abs dots"><span></span><span></span><span class="on"></span><span></span><span></span></div>
</section>

<!-- promo tiles -->
<div class="abs promo" style="left:76px;background:var(--orange)">
  <div class="thumb" role="img" aria-label="Green relay control board" style="background:linear-gradient(135deg,#3a9d57,#1e6b3a)"></div>
  <div class="pname">PRODUCT NAME</div><div class="save">SAVE UP TO 40%</div>
</div>
<div class="abs promo" style="left:425px;background:var(--blue)">
  <div class="thumb" role="img" aria-label="Rack network switch" style="width:250px;height:60px;margin-top:44px;background:linear-gradient(#c9ccd1,#6e737b)"></div>
  <div class="pname" style="color:var(--orange);margin-top:24px">PRODUCT NAME</div><div class="save">SAVE UP TO 40%</div>
</div>
<div class="abs promo" style="left:774px;background:var(--orange)">
  <div class="thumb" role="img" aria-label="Compact branch router" style="width:150px;background:linear-gradient(135deg,#4f7fa5,#2a4a66)"></div>
  <div class="pname">PRODUCT NAME</div><div class="save">SAVE UP TO 40%</div>
</div>

<!-- categories -->
<h2 class="abs section-title" style="top:1000px">PRODUCT CATEGORIES</h2>
<div class="abs cat" style="left:76px">
  <div class="img" role="img" aria-label="Ceiling wireless access point" style="background:var(--orange-soft)"></div>
  <div class="abs btn-orange" style="left:28px;top:82px;width:190px;height:54px;font-size:17px;justify-content:space-between;padding:0 6px 0 28px">VIEW ALL <span class="mark"></span></div>
  <div class="label warm">WIRELESS &amp; SECURITIES</div>
</div>
<div class="abs cat" style="left:342px">
  <div class="img" role="img" aria-label="Stacked network switches" style="background:linear-gradient(#f5f6f8,#dfe3e8)"></div>
  <div class="label">ROUTERS &amp; SWITCHES</div>
</div>
<div class="abs cat" style="left:608px">
  <div class="img" role="img" aria-label="Desk IP phone" style="background:linear-gradient(#f5f6f8,#dfe3e8)"></div>
  <div class="label">IP PHONES</div>
</div>
<div class="abs cat" style="left:872px">
  <div class="img" role="img" aria-label="SFP transceiver modules" style="background:linear-gradient(#f5f6f8,#dfe3e8)"></div>
  <div class="label">ACCESSORIES</div>
</div>

<!-- quote band -->
<section class="abs quote-band"></section>
<div class="abs agent" role="img" aria-label="Smiling support agent wearing a headset" style="background:linear-gradient(160deg,#f5b57a,#e98a3c 70%)"></div>
<div class="abs quote-title">REQUEST A QUOTE</div>
<div class="abs quote-line" style="left:150px;top:1556px;font-size:30px">
  <svg width="30" height="34" viewBox="0 0 24 24"><path d="M6 2l3 0 1.5 4.5-2 1.5a10 10 0 0 0 6 6l1.5-2 4.5 1.5v3a2 2 0 0 1-2 2A17 17 0 0 1 4 5a2 2 0 0 1 2-3z" fill="none" stroke="#222" stroke-width="1.8"/></svg>
  <span>(061) 02 5550 1234</span>
</div>
<div class="abs" style="left:128px;top:1612px;width:430px;font-size:17px;font-style:italic;color:#fff;line-height:1.6">Call today for a great price on new and used networking equipment</div>
<div class="abs heading" style="left:128px;top:1684px;font-size:34px;font-weight:600;color:#fff">OR EMAIL TO :</div>
<div class="abs quote-line" style="left:146px;top:1738px;font-size:28px">
  <svg width="40" height="30" viewBox="0 0 20 16"><rect x="1" y="1" width="18" height="14" rx="1" fill="none" stroke="#222" stroke-width="1.2"/><path d="M1 2l9 7 9-7" fill="none" stroke="#222" stroke-width="1.2"/></svg>
  <span>hello@netquarry-example.com</span>
</div>

<!-- stats -->
<h2 class="abs section-title" style="top:1864px">WELCOME TO NETQUARRY</h2>
<div class="abs stat" style="left:90px">
  <svg width="142" height="142" viewBox="0 0 142 142"><path d="M71 4a67 67 0 0 1 0 134" fill="none" stroke="#0b74c7" stroke-width="6"/><path d="M71 138a67 67 0 0 1 0-134" fill="none" stroke="#f7892e" stroke-width="6"/><text x="71" y="84" text-anchor="middle" font-family="Montserrat,sans-serif" font-size="40" font-weight="500" fill="#0b74c7">7</text></svg>
  <div class="label">Year of experience</div>
</div>
<div class="abs stat" style="left:374px">
  <svg width="142" height="142" viewBox="0 0 142 142"><path d="M71 4a67 67 0 0 1 0 134" fill="none" stroke="#0b74c7" stroke-width="6"/><path d="M71 138a67 67 0 0 1 0-134" fill="none" stroke="#f7892e" stroke-width="6"/><text x="71" y="84" text-anchor="middle" font-family="Montserrat,sans-serif" font-size="40" font-weight="500" fill="#0b74c7">99.5</text></svg>
  <div class="label">Positive feedback<br>on AuctionHub</div>
</div>
<div class="abs stat" style="left:624px">
  <svg width="142" height="142" viewBox="0 0 142 142"><path d="M71 4a67 67 0 0 1 0 134" fill="none" stroke="#0b74c7" stroke-width="6"/><path d="M71 138a67 67 0 0 1 0-134" fill="none" stroke="#f7892e" stroke-width="6"/><text x="71" y="84" text-anchor="middle" font-family="Montserrat,sans-serif" font-size="40" font-weight="500" fill="#0b74c7">300</text></svg>
  <div class="label">Client &amp; partners<br>around the world</div>
</div>
<div class="abs stat" style="left:880px">
  <svg width="142" height="142" viewBox="0 0 142 142"><path d="M71 4a67 67 0 0 1 0 134" fill="none" stroke="#0b74c7" stroke-width="6"/><path d="M71 138a67 67 0 0 1 0-134" fill="none" stroke="#f7892e" stroke-width="6"/><text x="71" y="84" text-anchor="middle" font-family="Montserrat,sans-serif" font-size="40" font-weight="500" fill="#0b74c7">1.250</text></svg>
  <div class="label">SKUs in inventory</div>
</div>

<!-- about -->
<section class="abs about">
  <h2>NETQUARRY</h2>
  <p style="top:94px">NetQuarry is an Australian-based company which sells used networking devices to coporates and other brokers in USA, Europe and other countries. We are the market leader in this space and currently have warehouses in Sydney and California. Most of our products are from VORTEL.</p>
  <p style="top:186px">Our competitive advantages come from lowest price in the market, flexible product configuration for different demands of customers, long time experience in the business and huge stock of inventory.</p>
  <div class="abs btn-orange" style="left:824px;top:104px;width:206px;height:58px;font-size:19px;justify-content:space-between;padding:0 6px 0 18px">READ MORE <span class="mark"></span></div>
</section>

<!-- why choose us -->
<h2 class="abs section-title" style="top:2568px">WHY CHOOSE US</h2>
<div class="abs why" style="left:76px;background:var(--orange)">
  <svg class="ico" width="100" height="110" viewBox="0 0 100 110" role="img" aria-label="Warranty seal"><circle cx="50" cy="55" r="46" fill="#fff"/><circle cx="50" cy="55" r="34" fill="none" stroke="#f7892e" stroke-width="3"/></svg>
  <div class="label">WARRANTY</div>
</div>
<div class="abs why" style="left:425px;background:var(--blue)">
  <svg class="ico" width="100" height="120" viewBox="0 0 100 120"><rect x="18" y="6" width="64" height="100" rx="6" fill="none" stroke="#fff" stroke-width="3.5"/><path d="M50 26l14 5v10c0 9-6 15-14 18-8-3-14-9-14-18V31z" fill="none" stroke="#fff" stroke-width="3"/><path d="M50 30v26M38 42h24" stroke="#fff" stroke-width="2"/><path d="M32 74h36M32 86h36" stroke="#fff" stroke-width="3"/></svg>
  <div class="label">PRIVACY STATEMENT</div>
</div>
<div class="abs why" style="left:774px;background:var(--orange)">
  <svg class="ico" width="100" height="120" viewBox="0 0 100 120"><path d="M20 10h46l16 16v82H20z" fill="none" stroke="#fff" stroke-width="3"/><path d="M66 10v16h16" fill="none" stroke="#fff" stroke-width="3"/><path d="M32 44h26M32 56h36M32 68h30" stroke="#fff" stroke-width="2.5"/><path d="M40 96l40-46 6 5-40 46-9 3z" fill="none" stroke="#fff" stroke-width="3"/></svg>
  <div class="label">TERMS OF TRADE</div>
</div>

<!-- footer -->
<svg class="abs waves" viewBox="0 0 1200 110" preserveAspectRatio="none">
  <path d="M0 40C150 -10 320 20 480 50S820 70 1000 30 1200 20 1200 20V110H0z" fill="#bfe2f7"/>
  <path d="M0 70C180 20 360 60 560 50S900 10 1200 50V110H0z" fill="#f7892e"/>
  <path d="M0 86C200 60 400 100 620 80S980 60 1200 86V110H0z" fill="#0e0e0e"/>
</svg>
<footer class="abs footer">
  <h4 style="left:76px">ABOUT US</h4>
  <div class="txt" style="left:76px;top:64px;width:228px">NetQuarry is an Australian-based company which sells used networking devices to coporates and other brokers in USA, Europe and other countries.</div>
  <div class="abs btn-orange" style="left:76px;top:240px;width:210px;height:58px;font-size:19px;justify-content:space-between;padding:0 6px 0 18px">READ MORE <span class="mark"></span></div>

  <h4 style="left:344px">CONTACT US</h4>
  <div class="frow" style="left:344px;top:64px">
    <svg width="20" height="26" viewBox="0 0 20 26"><path d="M10 25S2 15 2 9a8 8 0 0 1 16 0c0 6-8 16-8 16z" fill="none" stroke="#0b74c7" stroke-width="2"/><circle cx="10" cy="9" r="3" fill="none" stroke="#0b74c7" stroke-width="2"/></svg>
    <div><b style="color:#4aa6ea;font-size:16px">NETQUARRY</b><br>Unit 8/ 12 Harbour Rd<br>Westmead, NSW 2150.</div>
  </div>
  <div class="frow" style="left:344px;top:170px">
    <svg width="22" height="20" viewBox="0 0 24 24"><path d="M6 2l3 0 1.5 4.5-2 1.5a10 10 0 0 0 6 6l1.5-2 4.5 1.5v3a2 2 0 0 1-2 2A17 17 0 0 1 4 5a2 2 0 0 1 2-3z" fill="none" stroke="#0b74c7" stroke-width="2"/></svg>
    <div>(+61) 02 5550 1234 /<br>04 5550 7788</div>
  </div>
  <div class="frow" style="left:344px;top:232px">
    <svg width="22" height="18" viewBox="0 0 20 16"><rect x="1" y="1" width="18" height="14" rx="1" fill="none" stroke="#0b74c7" stroke-width="1.6"/><path d="M1 2l9 7 9-7" fill="none" stroke="#0b74c7" stroke-width="1.6"/></svg>
    <div>sales@netquarry-example.com.au</div>
  </div>
  <div class="frow" style="left:344px;top:274px">
    <svg width="22" height="22" viewBox="0 0 22 22"><circle cx="11" cy="11" r="9" fill="none" stroke="#0b74c7" stroke-width="2"/><path d="M11 5v6l4 3" fill="none" stroke="#0b74c7" stroke-width="2"/></svg>
    <div>8:30 am -5:30 pm/ Mon-Fri<br>(UTC + 10)</div>
  </div>
  <div class="frow" style="left:344px;top:334px;font-size:13.5px;line-height:1.5">
    <span style="width:22px;height:12px;background:#0b74c7;display:inline-block;margin-top:5px"></span>
    <div>http://stores.auctionhub-example.com.au/<br>netquarry55501234/</div>
  </div>

  <h4 style="left:620px">PAYMENT METHODS</h4>
  <div class="abs" style="left:620px;top:70px;display:flex;gap:10px">
    <span class="card" role="img" aria-label="Card payment accepted" style="background:#e8e8e8"></span>
    <span class="card" role="img" aria-label="Online wallet payment accepted" style="background:#e8e8e8"></span>
    <span class="card" role="img" aria-label="Card payment accepted" style="background:#e8e8e8"></span>
  </div>

  <h4 style="left:874px">WHY US</h4>
  <div class="why-row" style="top:64px"><span class="b"><svg width="16" height="22" viewBox="0 0 16 22"><path d="M12 5c-1-2-8-2-8 2s8 2 8 7-7 4-8 2M8 1v20" fill="none" stroke="#fff" stroke-width="2.2"/></svg></span>100% wholesale Price</div>
  <div class="why-row" style="top:122px"><span class="b"><svg width="20" height="20" viewBox="0 0 20 20"><path d="M2 9h4v9H2zM7 18h8l3-7V9h-6l1-5-2-2-4 6z" fill="#fff"/></svg></span>100% Quality Assurance</div>
  <div class="why-row" style="top:180px"><span class="b">FREE</span>Free Support</div>
  <div class="why-row" style="top:238px"><span class="b"><svg width="18" height="20" viewBox="0 0 18 20"><path d="M9 1l7 3v6c0 5-3 8-7 9-4-1-7-4-7-9V4z" fill="#fff"/></svg></span>Free Money Back Guarantee</div>
  <div class="why-row" style="top:296px"><span class="b"><svg width="18" height="20" viewBox="0 0 18 20"><path d="M9 1l7 3v6c0 5-3 8-7 9-4-1-7-4-7-9V4z" fill="none" stroke="#fff" stroke-width="2"/><path d="M5 10l3 3 5-6" fill="none" stroke="#fff" stroke-width="2"/></svg></span>Flexible Payment</div>
</footer>
<div class="abs bottom">© 2017 NetQuarry Pty. Ltd - All Rights Reserved</div>

</body>
</html>
```